business cards for Pollenwick Systems

Require business card design for a technology company supplying systems and networking products to the Data Centre market. Design should be clean and simple, professional and elegant.

the company website is www.pollenwicksystems-demo.com

Target Market(s)

data centres

Industry/Entity Type

Business

Contact Information for Business Card

color scheme is aqua and qhite

Font styles to use
Serif

Colors
85cae6
ffffff

Requirements
Must have
• Business Card design for 2 employees

```html
<!DOCTYPE html>
<html lang="en">
<head>
<meta charset="utf-8">
<title>Pollenwick Systems business cards</title>
<link href="https://fonts.googleapis.com/css2?family=Montserrat:wght@400;500;700&display=swap" rel="stylesheet">
<style>
  :root {
    --stage: #3a3a3c;
    --card: #161617;
    --card-edge: #0b0b0c;
    --aqua: #85cae6;
    --white: #ffffff;
    --silver: #b9bbbe;
    --text: #e8e8e8;
  }
  * { box-sizing: border-box; margin: 0; padding: 0; }
  html, body { width: 1200px; height: 864px; overflow: hidden; }
  body {
    background: var(--stage);
    font-family: "Montserrat", Arial, sans-serif;
    position: relative;
  }
  .card {
    position: absolute;
    top: 278px;
    width: 540px;
    height: 309px;
    background: var(--card);
    border: 1px solid var(--card-edge);
    box-shadow: 0 14px 34px rgba(0,0,0,.45);
  }
  .card--front { left: 40px; }
  .card--back { left: 620px; }

  .wordmark {
    font-weight: 700;
    text-transform: uppercase;
    line-height: 1;
  }
  .card--front .wordmark {
    position: absolute;
    left: 0; right: 0; top: 118px;
    text-align: center;
    color: var(--silver);
    font-size: 34px;
    letter-spacing: 3px;
  }
  .card--front .wordmark span {
    display: block;
    font-size: 15px;
    letter-spacing: 12px;
    margin-top: 8px;
  }
  .card--back .wordmark {
    position: absolute;
    right: 30px; top: 30px;
    text-align: right;
    color: var(--aqua);
    font-size: 24px;
    letter-spacing: 2px;
  }
  .card--back .wordmark span {
    display: block;
    font-size: 11px;
    letter-spacing: 8px;
    margin-top: 6px;
  }

  .rule {
    position: absolute;
    left: 30px; right: 30px; top: 190px;
    height: 1px;
    background: var(--aqua);
  }
  .person {
    position: absolute;
    left: 30px; top: 146px;
  }
  .person__name {
    color: var(--aqua);
    font-size: 21px;
    font-weight: 500;
    letter-spacing: .5px;
  }
  .person__role {
    color: var(--text);
    font-size: 14px;
    margin-top: 2px;
  }
  .contacts {
    position: absolute;
    left: 30px; top: 212px;
    list-style: none;
    color: var(--text);
    font-size: 14px;
  }
  .contacts li {
    display: flex;
    align-items: center;
    gap: 8px;
    height: 22px;
  }
  .contacts svg { width: 13px; height: 13px; flex: none; }
  .address {
    position: absolute;
    right: 30px; top: 202px;
    text-align: right;
    color: var(--text);
    font-size: 14px;
    line-height: 1.4;
    font-style: normal;
  }
</style>
</head>
<body>
  <section class="card card--front" aria-label="Card front">
    <div class="wordmark">Pollenwick<span>Systems</span></div>
  </section>

  <section class="card card--back" aria-label="Card back">
    <div class="wordmark">Pollenwick<span>Systems</span></div>

    <div class="person">
      <div class="person__name">MARCUS HALE</div>
      <div class="person__role">President</div>
    </div>

    <div class="rule"></div>

    <ul class="contacts">
      <li>
        <svg viewBox="0 0 16 16" aria-hidden="true"><path d="M3 1.5l3 3-1.6 1.7c.9 2 2.4 3.5 4.4 4.4L10.5 9l3 3-1.8 2.2C6.5 13.5 2.5 9.5 1.8 3.3z" fill="var(--aqua)"/></svg>
        +61 3 9000 4127
      </li>
      <li>
        <svg viewBox="0 0 16 16" aria-hidden="true"><rect x="1" y="3" width="14" height="10" fill="var(--aqua)"/><path d="M1 3l7 6 7-6" fill="none" stroke="var(--card)" stroke-width="1.4"/></svg>
        info@pollenwicksystems-demo.com
      </li>
      <li>
        <svg viewBox="0 0 16 16" aria-hidden="true"><g fill="none" stroke="var(--aqua)" stroke-width="1.3"><circle cx="8" cy="8" r="6.5"/><ellipse cx="8" cy="8" rx="2.8" ry="6.5"/><path d="M1.5 8h13M2.5 5h11M2.5 11h11"/></g></svg>
        pollenwicksystems-demo.com
      </li>
    </ul>

    <address class="address">
      14B Carrow Lane<br>
      Hollybank, 3199<br>
      Australia
    </address>
  </section>
</body>
</html>
```